New professional looking flyer for company

I need our flyer updated my flyer is the Ruv flyer Have attached current flyer so you know what services need to be listed. Want it to be in mainly dark colours like black and dark grey with pops of light grey, silver or white. i have added several photos for you to choose which ones work best with your design would like The photos to be in colour for the flyer. But can have a mix of greyscale if that works for your design j have attached another companies flyers as design ideas to show what I am looking for

Target Market(s)

new clients

Industry/Entity Type

transport and earthmoving

Colors

Designer to choose colors to be used in the design.

Requirements
Nice to have
• Look professional
Should not have
• No orange or red or green

```html
<!DOCTYPE html>
<html lang="en">
<head>
<meta charset="UTF-8">
<title>Ruv Pty Ltd – Our Services</title>
<link href="https://fonts.googleapis.com/css2?family=Roboto+Condensed:wght@400;700&display=swap" rel="stylesheet">
<style>
  :root{
    --page-bg:#d6d6d6;
    --flyer-black:#0b0b0c;
    --flyer-charcoal:#1c1d20;
    --photo-dusk:#3a3b3f;
    --photo-road:#2a2b2e;
    --silver-light:#f2f2f2;
    --silver-mid:#b9b9b9;
    --silver-dark:#7d7d7d;
    --text-white:#ffffff;
    --text-soft:#e4e4e4;
    --text-dark:#141414;
    --pill-grey:rgba(200,200,200,0.78);
  }
  *{margin:0;padding:0;box-sizing:border-box}
  html,body{width:1199px;height:1200px;overflow:hidden;background:var(--page-bg)}
  body{position:relative;font-family:"Roboto Condensed",Arial,sans-serif}
  .flyer{
    position:absolute;left:194px;top:75px;width:813px;height:1052px;
    background:var(--flyer-black);overflow:hidden;
    box-shadow:0 3px 10px rgba(0,0,0,0.35);
  }
  .flyer__texture{
    position:absolute;inset:0 0 auto 0;height:560px;
    background:radial-gradient(ellipse at 50% 0%,#26272a 0%,#141416 55%,var(--flyer-black) 100%);
  }
  .flyer__photo{
    position:absolute;left:0;right:0;top:520px;bottom:0;
    background:linear-gradient(180deg,var(--flyer-black) 0%,var(--photo-dusk) 22%,#4a4b50 45%,var(--photo-road) 80%,#161618 100%);
  }
  .brand{position:absolute;left:0;right:0;top:58px;text-align:center;color:var(--silver-mid)}
  .brand__rule{position:absolute;height:2px;background:var(--silver-mid)}
  .brand__rule--top{left:225px;width:358px;top:4px}
  .brand__rule--left{left:225px;width:130px;top:178px}
  .brand__rule--right{left:463px;width:120px;top:178px}
  .brand__name{
    display:block;margin-top:14px;font-weight:700;font-size:124px;line-height:1;
    letter-spacing:4px;color:var(--silver-mid);
  }
  .brand__suffix{
    display:block;margin-top:14px;font-weight:700;font-size:32px;line-height:1;color:var(--silver-mid);
  }
  .fleet-photo{
    position:absolute;left:204px;top:275px;width:326px;height:118px;
    background:linear-gradient(90deg,#8a8070 0%,#b8ab8e 40%,#2e2f33 70%,#c9b98a 100%);
    border-radius:4px;
  }
  .section-banner{position:absolute;left:181px;top:393px;width:447px;height:78px}
  .section-banner__title{
    position:absolute;inset:0;display:flex;align-items:center;justify-content:center;
    padding-left:20px;font-weight:700;font-size:50px;color:var(--text-dark);letter-spacing:0.5px;
  }
  .services{position:absolute;list-style:none;color:var(--text-white);font-weight:700;font-size:22.5px;line-height:1.1}
  .services--left{left:52px;top:526px}
  .services--right{left:500px;top:526px}
  .services li{position:relative;padding-left:28px;height:46.6px}
  .services li svg{position:absolute;left:0;top:5px}
  .services li.services__two-line{height:auto}
  .services__extra{
    position:absolute;left:526px;top:800px;color:var(--text-soft);font-size:21px;font-weight:400;
  }
  .quote-pill{
    position:absolute;left:81px;top:870px;width:650px;height:79px;border-radius:40px;
    background:var(--pill-grey);display:flex;align-items:center;justify-content:center;
    text-align:center;color:var(--text-dark);font-size:21px;line-height:1.25;
  }
</style>
</head>
<body>
  <main class="flyer">
    <div class="flyer__texture" role="img" aria-label="Dark curved dotted texture background"></div>
    <div class="flyer__photo" role="img" aria-label="Photo of a white prime mover truck on an outback highway at dusk"></div>

    <header class="brand">
      <span class="brand__rule brand__rule--top"></span>
      <span class="brand__name">Ruv</span>
      <span class="brand__suffix">Pty Ltd</span>
      <span class="brand__rule brand__rule--left"></span>
      <span class="brand__rule brand__rule--right"></span>
    </header>

    <div class="fleet-photo" role="img" aria-label="Photo of a road train tanker truck"></div>

    <div class="section-banner">
      <svg width="447" height="78" viewBox="0 0 447 78" aria-hidden="true">
        <defs>
          <linearGradient id="silverBand" x1="0" y1="0" x2="1" y2="1">
            <stop offset="0" stop-color="#9a9a9a"/>
            <stop offset="0.35" stop-color="#f4f4f4"/>
            <stop offset="0.65" stop-color="#c4c4c4"/>
            <stop offset="1" stop-color="#eeeeee"/>
          </linearGradient>
        </defs>
        <path d="M0 0 H395 Q447 0 447 78 H60 Q20 78 0 0 Z" fill="url(#silverBand)"/>
      </svg>
      <h1 class="section-banner__title">OUR SERVICES</h1>
    </div>

    <ul class="services services--left">
      <li><svg width="16" height="16" viewBox="0 0 16 16"><circle cx="8" cy="8" r="6.5" fill="none" stroke="#fff" stroke-width="1.4"/><path d="M5 8.2l2 2 4-4.2" fill="none" stroke="#fff" stroke-width="1.4"/></svg>Over size loads/Hot Shot Loads</li>
      <li><svg width="16" height="16" viewBox="0 0 16 16"><circle cx="8" cy="8" r="6.5" fill="none" stroke="#fff" stroke-width="1.4"/><path d="M5 8.2l2 2 4-4.2" fill="none" stroke="#fff" stroke-width="1.4"/></svg>Heavy Vehicle Recovery Services</li>
      <li><svg width="16" height="16" viewBox="0 0 16 16"><circle cx="8" cy="8" r="6.5" fill="none" stroke="#fff" stroke-width="1.4"/><path d="M5 8.2l2 2 4-4.2" fill="none" stroke="#fff" stroke-width="1.4"/></svg>Potable Water Deliveries</li>
      <li><svg width="16" height="16" viewBox="0 0 16 16"><circle cx="8" cy="8" r="6.5" fill="none" stroke="#fff" stroke-width="1.4"/><path d="M5 8.2l2 2 4-4.2" fill="none" stroke="#fff" stroke-width="1.4"/></svg>Road Building/Maintenance</li>
      <li><svg width="16" height="16" viewBox="0 0 16 16"><circle cx="8" cy="8" r="6.5" fill="none" stroke="#fff" stroke-width="1.4"/><path d="M5 8.2l2 2 4-4.2" fill="none" stroke="#fff" stroke-width="1.4"/></svg>Earthworks</li>
      <li><svg width="16" height="16" viewBox="0 0 16 16"><circle cx="8" cy="8" r="6.5" fill="none" stroke="#fff" stroke-width="1.4"/><path d="M5 8.2l2 2 4-4.2" fill="none" stroke="#fff" stroke-width="1.4"/></svg>Sand &amp; Metal Supply &amp; Cartage</li>
    </ul>

    <ul class="services services--right">
      <li><svg width="16" height="16" viewBox="0 0 16 16"><circle cx="8" cy="8" r="6.5" fill="none" stroke="#fff" stroke-width="1.4"/><path d="M5 8.2l2 2 4-4.2" fill="none" stroke="#fff" stroke-width="1.4"/></svg>Road Train Tippers</li>
      <li><svg width="16" height="16" viewBox="0 0 16 16"><circle cx="8" cy="8" r="6.5" fill="none" stroke="#fff" stroke-width="1.4"/><path d="M5 8.2l2 2 4-4.2" fill="none" stroke="#fff" stroke-width="1.4"/></svg>Road Train Tankers</li>
      <li><svg width="16" height="16" viewBox="0 0 16 16"><circle cx="8" cy="8" r="6.5" fill="none" stroke="#fff" stroke-width="1.4"/><path d="M5 8.2l2 2 4-4.2" fill="none" stroke="#fff" stroke-width="1.4"/></svg>Road Train Flat Tops</li>
      <li><svg width="16" height="16" viewBox="0 0 16 16"><circle cx="8" cy="8" r="6.5" fill="none" stroke="#fff" stroke-width="1.4"/><path d="M5 8.2l2 2 4-4.2" fill="none" stroke="#fff" stroke-width="1.4"/></svg>Drop Deck Trailers</li>
      <li class="services__two-line"><svg width="16" height="16" viewBox="0 0 16 16"><circle cx="8" cy="8" r="6.5" fill="none" stroke="#fff" stroke-width="1.4"/><path d="M5 8.2l2 2 4-4.2" fill="none" stroke="#fff" stroke-width="1.4"/></svg>Main Site accredited<br>equipment &amp; Operators</li>
    </ul>

    <p class="services__extra">Traffic Management</p>

    <p class="quote-pill">We offer a large range of services not listed so<br>Call us today for a personalised quote to suit your needs.</p>
  </main>
</body>
</html>
```